Secret agents need a new website

We organize child birthdays with a special agents in london & Bristol.

Current design does not grab people attention, and they leave website too soon.

Colors. Up to 3 main colors, but maybe black + green + white, or blact + red + white, would suit our secret operations website.

Current website:
www.jollyfete.co.uk

Dear designers, thanks very much for working on our design.

Please try to make like a SPECIAL YOUNG AGENT TRAINING WEBSITE, all other
entertainers have childish websites, and we want to differentiate from them.

Not sure if it helps, but I like this design very much:

Guys,

I am looking for spy/secret agent/action themed design. You submitting awesome designs, and if I have another business, I just choose any of them at it would be perfect. But I want spy/secret agent/action themed.

Please feel free to add elements like:

1. Yellow, or RED line CRIME SCENE DO NOT CROSS
2. Some words or phrases can be black background - white text. 
3. Some stamps like this:
http://www.pixelvarn.com/pic-71829455/stock-vector-various-security-rubber-stamps-top-secret-confidential-etc.html?src=pQt8Lm-zRwXeN3a-k57HvB-1-16

4.spy guys http://www.pixelvarn.com/pic-48213907/stock-vector-detective-in-trench-coat-retro-clip-art.html?src=hwTbRsJePo4K2nxtmcVfUQ-1-9

Do not make too much elements, I like simple designs, less details.  

PLEASE NO CHILDS WITH GUNS, and better NO GUNS at all. 

Target Market(s)

Audience: Woman, but should look cool for kids too.
(Please DO NOT make design childish)

Requirements
Must have
• Please take a look at current website
• 1. Texts should be easy to read and not too small.
• 2. White/bright background
• 3. Lead form should stay on page
• 4. Header, and footer should be not too big.
• 5. Infographic is not needed
• Extra elements
• 1. Company blog
• 2. Client zone
• 3. Venue finder
• 4. How to pay deposit
Nice to have
• We accept
• Coinvey
• morwells
• (please browse logos)
• On header would be better to use
• JollyFete.co.uk
• But also add somethere, in association with Tin-kettle.co.uk.
• Please use logo with .co.uk
• In archive you will find without background if needed too.

```html
<!DOCTYPE html>
<html lang="en">
<head>
<meta charset="utf-8">
<title>Top Secret Spy Party</title>
<link href="https://fonts.googleapis.com/css2?family=Raleway:wght@300;400;600;700;800&display=swap" rel="stylesheet">
<style>
:root{
  --red:#c8202c;
  --red-dark:#8e1018;
  --green:#5cb82e;
  --black:#111111;
  --white:#ffffff;
  --grey:#666666;
  --pink:#ff9aa0;
  --line:#cccccc;
}
*{box-sizing:border-box;margin:0;padding:0}
html,body{width:1200px;height:3168px;overflow:hidden}
body{position:relative;background:var(--white);font-family:'Raleway',sans-serif;color:var(--grey)}
.abs{position:absolute}

/* header */
.brand{left:80px;top:50px;display:flex;align-items:center;gap:18px}
.brand-mark{width:70px;height:70px;background:var(--green)}
.brand-name{font-size:44px;font-weight:800;color:var(--black)}
.balloons{left:0;top:0}
.balloon-text{font-family:'Raleway',sans-serif;fill:var(--white);font-weight:800;text-anchor:middle}
.main-nav{left:540px;top:372px;width:660px;height:40px;background:var(--red);display:flex;align-items:center;gap:36px;padding-left:40px}
.main-nav a{color:var(--white);font-size:14px;font-weight:700;text-decoration:none;letter-spacing:.5px}

/* hero */
.hero-pitch{left:80px;top:480px;width:460px;height:320px;background:var(--green);padding:30px 28px;color:var(--white)}
.hero-pitch .quote{font-size:25px;font-weight:300;line-height:1.25}
.hero-pitch .title{font-size:32px;font-weight:800;margin:6px 0 22px}
.hero-pitch .sub{font-size:18px;font-weight:400;line-height:1.3}
.hero-pitch .sub b{font-weight:700}
.video{left:580px;top:480px;width:540px;height:320px;background:var(--black)}

/* intro */
.photo{background:linear-gradient(135deg,#c9a98a,#6d7a8c)}
.badge-art{background:linear-gradient(135deg,#2a2a2a,#777)}
.intro{left:580px;top:840px;width:540px;font-size:15.5px;line-height:1.5}
.intro p{margin-bottom:16px}
.tag{background:var(--black);color:var(--white);font-weight:700;padding:1px 6px}
.spy-id{left:580px;top:1346px;width:220px;height:44px;background:var(--green);color:var(--white);font-size:22px;font-weight:700;padding:8px 20px;clip-path:polygon(0 0,92% 0,100% 100%,0 100%)}

/* faq band */
.band{left:0;top:1420px}
.faq{left:60px;top:1470px;width:480px;color:var(--white)}
.faq h3{color:var(--pink);font-size:24px;font-weight:400;line-height:1.2;margin-bottom:8px}
.faq h3 b{font-weight:800;color:var(--white)}
.faq p{font-size:14px;line-height:1.45;margin-bottom:22px}
.faq strong{font-weight:800}
.infographic{left:580px;top:1500px;width:560px;height:740px;background:linear-gradient(160deg,#f7a21b 0%,#f5e9c8 40%,#4fb6c9 100%)}

/* quote form */
.quote-form{left:580px;top:2300px;width:560px}
.quote-form h2{color:var(--green);font-size:40px;font-weight:800;margin-bottom:36px}
.field{display:flex;align-items:center;margin-bottom:22px}
.field label{width:200px;font-size:18px;color:var(--grey)}
.field span{width:330px;height:38px;border:1px solid var(--line)}
.form-foot{display:flex;justify-content:space-between;align-items:center;margin-top:30px}
.form-foot p{font-size:17px;line-height:1.4;width:280px}
.btn{background:var(--black);color:var(--white);font-weight:800;font-size:20px;padding:14px 30px;letter-spacing:1px}

/* footer */
.footer-nav{left:0;top:3060px;width:1200px;display:flex;justify-content:center;gap:12px}
.footer-nav a{background:var(--black);color:var(--white);font-size:15px;font-weight:700;padding:5px 12px;text-decoration:none}
.copyright{left:0;top:3106px;width:1200px;text-align:center;font-size:15px;color:var(--grey)}
</style>
</head>
<body>

<header>
  <div class="abs brand"><span class="brand-mark"></span><span class="brand-name">Tin-kettle.co.uk</span></div>

  <svg class="abs balloons" width="1200" height="420" viewBox="0 0 1200 420">
    <g stroke="var(--black)" stroke-width="2" fill="none">
      <path d="M730 340 C722 355 738 362 730 372"/>
      <path d="M820 355 C812 362 826 366 820 372"/>
      <path d="M1020 260 C1008 300 1032 330 1020 372"/>
    </g>
    <circle cx="730" cy="250" r="90" fill="var(--black)"/>
    <text class="balloon-text" x="730" y="260" font-size="28">ENQUIRY</text>
    <circle cx="820" cy="300" r="55" fill="var(--black)"/>
    <circle cx="800" cy="300" r="15" fill="var(--white)"/>
    <circle cx="840" cy="300" r="15" fill="var(--white)"/>
    <circle cx="1020" cy="140" r="120" fill="var(--black)"/>
    <text class="balloon-text" x="1020" y="130" font-size="30" font-weight="400">CALL US</text>
    <text class="balloon-text" x="1020" y="172" font-size="34">3608 4417</text>
  </svg>

  <nav class="abs main-nav">
    <a href="#">HOME</a><a href="#">EQUIPMENT</a><a href="#">INVITATIONS</a><a href="#">PARTY</a><a href="#">BAGS PRICES</a>
  </nav>
</header>

<section>
  <div class="abs hero-pitch">
    <p class="quote">I wanted a kids birthday party with a difference and then I found the</p>
    <p class="title">Top Secret Spy Party</p>
    <p class="sub">Capture your kids imagination with <b>a Spy Birthday Party</b> in London, Bristol</p>
  </div>
  <div class="abs video">
    <svg width="540" height="320" viewBox="0 0 540 320"><polygon points="250,130 250,190 300,160" fill="var(--white)"/></svg>
  </div>
</section>

<section>
  <div class="abs photo" style="left:80px;top:840px;width:148px;height:130px" role="img" aria-label="Children at a spy party"></div>
  <div class="abs photo" style="left:236px;top:840px;width:148px;height:130px" role="img" aria-label="Children at a spy party"></div>
  <div class="abs photo" style="left:392px;top:840px;width:148px;height:130px" role="img" aria-label="Children at a spy party"></div>
  <div class="abs photo" style="left:80px;top:978px;width:148px;height:130px" role="img" aria-label="Children at a spy party"></div>
  <div class="abs photo" style="left:236px;top:978px;width:148px;height:130px" role="img" aria-label="Children at a spy party"></div>
  <div class="abs photo" style="left:392px;top:978px;width:148px;height:130px" role="img" aria-label="Children at a spy party"></div>
  <div class="abs badge-art" style="left:80px;top:1140px;width:225px;height:210px" role="img" aria-label="Spy school badge"></div>
  <div class="abs badge-art" style="left:315px;top:1140px;width:225px;height:210px;background:linear-gradient(135deg,#eeeeee,#9a9a9a)" role="img" aria-label="Spy school certificate"></div>

  <div class="abs intro">
    <p>Every parent wants to give their child the best birthday party, but we don't always have the time to plan and prepare for an extra special birthday party with the wow factor.</p>
    <p>We created this Spy party to be fun from beginning to end. Your child will send their guests coded <span class="tag">TOP SECRET INVITATIONS</span> to a party where they will take part in Secret Agent Training. The children will be so excited that they won't be able to stop talking about it.</p>
    <p>At the party all the children will become special agents, trying out <span class="tag">SPY GEAR</span> and finding out how to be a good spy in our fun secret agent games. It's a great way to get the children interested in new things, working together in teams and using their imagination. Every child that takes part will receive a Spy School Secret Agent certificate and <span class="tag">SPY PARTY BAG</span>. Make every child happy and continue the fun with their friends at home and at school.</p>
  </div>
  <div class="abs spy-id">Spy ID example</div>
</section>

<section>
  <svg class="abs band" width="1200" height="1240" viewBox="0 0 1200 1240">
    <defs>
      <linearGradient id="bandFill" x1="0" y1="0" x2="0" y2="1">
        <stop offset="0" stop-color="var(--red)"/>
        <stop offset="1" stop-color="var(--red-dark)"/>
      </linearGradient>
    </defs>
    <polygon points="0,0 1200,0 1200,860 560,860 560,1140 0,1210" fill="url(#bandFill)"/>
  </svg>

  <div class="abs faq">
    <h3>How many children can come to a Spy Birthday Party?</h3>
    <p>We provide parties for groups of up to 40 children. For groups of up to 15 we will provide one <strong>ENTERTAINER</strong>, for larger groups we will provide more <strong>ENTERTAINERS</strong> to ensure all the children get a great experience.</p>
    <h3>How old should the children be?</h3>
    <p>The Spy Birthday party is aimed at children aged 6-11, but we can adapt it for younger ones too.</p>
    <h3>Where can we have a Spy Birthday Party?</h3>
    <p>You can have a Spy Birthday Party anywhere, at your home, at a cafe or a church hall. If you need help finding a venue let us know and we can help find a suitable place.</p>
    <h3>How much does it cost?</h3>
    <p>The cost depends on how many children will be taking part. For groups up to 15, with one entertainer running the party, it costs <strong>£175.00</strong>. For larger groups have a look at our <strong>PRICES</strong>.</p>
    <h3>Who are our <b>ENTERTAINERS</b>?</h3>
    <p>All our <strong>ENTERTAINERS</strong> are CRB checked and are fully trained to organise this type of birthday. After every party we ask our clients for feedback on the event, which helps our entertainers to continually evaluate and improve their performance.</p>
    <h3>Is it the great party?</h3>
    <p>Many of our bookings come through recommendation. We have previous clients that would be happy to share their experience of a Spy Birthday Party. If you would like to talk to them let us know. You can also see some of our <strong>CLIENT FEEDBACK</strong>.</p>
    <p>We'd like to help you organise a party your child will remember. We appreciate that people have busy lives and organising a party can be hard work, so let us make it easy for you.</p>
    <p>Please fill in your information below, or call us and we can check our availability on your chosen date.</p>
  </div>

  <div class="abs infographic" role="img" aria-label="Top Secret party packages and ordering steps"></div>
</section>

<section class="abs quote-form">
  <h2>Request a quote now!</h2>
  <div class="field"><label>Your name</label><span></span></div>
  <div class="field"><label>Your e-mail</label><span></span></div>
  <div class="field"><label>Your city</label><span></span></div>
  <div class="field"><label>Your phone</label><span></span></div>
  <div class="form-foot">
    <p>We will respond within 24 hours Monday - Friday</p>
    <span class="btn">ENQUIRY</span>
  </div>
</section>

<svg class="abs" style="left:0;top:2560px" width="480" height="500" viewBox="0 0 480 500">
  <path d="M230 400 C215 440 245 460 230 500" stroke="var(--black)" stroke-width="2" fill="none"/>
  <circle cx="230" cy="210" r="190" fill="var(--black)"/>
  <text class="balloon-text" x="230" y="190" font-size="30" font-weight="400">Or just give us</text>
  <text class="balloon-text" x="230" y="228" font-size="30" font-weight="400">a call</text>
  <text class="balloon-text" x="230" y="276" font-size="40">3608 4417</text>
</svg>

<footer>
  <nav class="abs footer-nav"><a href="#">CONTACT US</a><a href="#">ABOUT US</a><a href="#">TERMS AND CONDITIONS</a></nav>
  <p class="abs copyright">Copyright © 2010-2013 Starlit Events Ltd.</p>
</footer>

</body>
</html>
```